Brochure Design Oakridge Capital Partners

Create a brochure, which sells my business. Utilise the website www.oakridgecapitalpartners.example for the details that need to go into the brochure. I would like 2 designs, one for a 4 page brochure and the other for a two page brochure (focus firstly on the 4 page).

The focus points are our 4 year rent guarantee and also out pitch that we are invested with them. Please see the website.

Need to focus on the main points as per the website, can use text from the website and the graphics where suitable.

On the 4 page brochure, first 3 pages to be info as per the website. On the 4 page of the brochure I would like the information included on the final 2 pages of the attached document (the investment property example). Please shrink this down, you do not need to include all the wording more so the figures.

The colours of the brochure to be blue, white and black

Target Market(s)

Property Investors

Industry/Entity Type

Business

Colors
0355a3
ffffff

Requirements
Must have
• Must have the main info on the website, (4 year rent guarantee) 'We are invested with you'
Nice to have
• Professional look

```html
<!DOCTYPE html>
<html lang="en">
<head>
<meta charset="utf-8">
<title>Oakridge Capital Partners – Brochure Spread</title>
<link rel="stylesheet" href="https://fonts.googleapis.com/css2?family=Questrial&family=Arimo:wght@400;700&display=swap">
<style>
  :root {
    --blue: #23a6e0;
    --blue-deep: #0355a3;
    --ink: #1b1b1b;
    --text: #3a3a3a;
    --white: #ffffff;
    --grey-band: #d9d9d9;
    --night: #1d232b;
  }
  * { margin: 0; padding: 0; box-sizing: border-box; }
  html, body { width: 1200px; height: 777px; overflow: hidden; background: var(--white); }
  .spread { position: relative; width: 1200px; height: 777px; overflow: hidden; font-family: "Arimo", Arial, sans-serif; color: var(--text); }
  .abs { position: absolute; }
  .heading { font-family: "Questrial", "Century Gothic", sans-serif; }

  .room-backdrop { left: 0; top: 0; width: 1200px; height: 777px;
    background: radial-gradient(ellipse at 40% 55%, #eceff1 0%, #f6f7f8 45%, #ffffff 80%),
                linear-gradient(180deg, #f3f4f5 0%, #e9ebed 100%); }

  .tagline-bar { top: 10px; height: 35px; background: var(--blue); color: var(--white);
    font-family: "Questrial", sans-serif; font-size: 16px; line-height: 35px; }
  .tagline-bar.left { left: 0; width: 378px; padding-left: 46px; }
  .tagline-bar.right { left: 598px; width: 602px; text-align: right; padding-right: 24px; }
  .accent-rule { height: 8px; background: var(--ink); top: 45px; }

  .brand { display: flex; align-items: center; gap: 10px; font-family: "Questrial", sans-serif; color: var(--ink); font-size: 15px; line-height: 1.1; }
  .brand-square { width: 30px; height: 30px; background: var(--ink); flex: none; }

  .service-panel { left: 300px; top: 56px; width: 288px; height: 209px; }
  .panel-tab { left: 315px; top: 255px; width: 36px; height: 36px; background: var(--blue); }

  .intro-title { left: 36px; top: 160px; color: var(--blue); font-size: 33px; }
  .intro-sub { left: 38px; top: 195px; color: var(--blue); font-size: 21px; }
  .intro-copy { left: 40px; top: 225px; width: 260px; font-size: 10px; line-height: 1.3; color: var(--ink); }

  .padlock { left: 30px; top: 272px; width: 148px; height: 166px; border-radius: 40px 40px 20px 20px;
    background: radial-gradient(circle at 50% 65%, #4a7fc0 0%, #2a5796 45%, #b9c3cc 75%, transparent 76%); }

  .invested-band { left: 186px; top: 302px; width: 414px; height: 77px; background: var(--grey-band); padding: 8px 0 0 16px; }
  .invested-band .big { color: var(--blue); font-size: 35px; line-height: 1; }
  .invested-band .small { color: var(--ink); font-size: 18px; margin-left: 4px; margin-top: 4px; }

  .kicker { font-size: 13px; color: var(--ink); }
  .guarantee-label { left: 195px; top: 403px; }
  .guarantee-title { left: 195px; top: 422px; font-size: 26px; color: var(--ink); }

  .guarantee-copy { left: 32px; top: 463px; width: 565px; font-size: 10.6px; line-height: 1.3; color: var(--ink); }
  .guarantee-copy p { margin-bottom: 13px; }

  .risk-bar { left: 0; top: 623px; height: 38px; width: 325px; background: var(--blue); color: var(--white);
    font-size: 21px; line-height: 38px; padding-left: 40px; }
  .risk-rule { left: 325px; top: 623px; width: 275px; height: 38px; background: var(--ink); }

  .benefit { top: 680px; width: 140px; text-align: center; }
  .benefit-icon { width: 40px; height: 40px; border-radius: 50%; background: var(--blue); margin: 0 auto 6px; display: flex; align-items: center; justify-content: center; }
  .benefit-label { font-size: 14.5px; color: var(--ink); font-family: "Arimo", sans-serif; }

  .site-footer { left: 0; top: 753px; width: 1200px; height: 24px; background: var(--blue); }
  .footer-url { top: 753px; width: 600px; text-align: center; font-size: 10px; letter-spacing: 3.2px; line-height: 24px; color: var(--ink); }

  .page-title { left: 627px; top: 76px; font-size: 32px; color: var(--blue); }
  .right-brand { left: 975px; top: 62px; }

  .property { left: 627px; width: 355px; }
  .property .tag { font-size: 10.5px; color: var(--blue); }
  .property .name { font-size: 16.5px; color: var(--ink); margin: 2px 0 10px; font-family: "Arimo", sans-serif; }
  .property p { font-size: 10.4px; line-height: 1.3; text-align: justify; color: var(--ink); margin-bottom: 12px; }

  .tablet-view { left: 995px; width: 192px; border-radius: 10px; }
</style>
</head>
<body>
<main class="spread">
  <div class="abs room-backdrop" role="img" aria-label="Soft faded living room interior photo behind the spread"></div>

  <!-- Left page -->
  <div class="abs tagline-bar left">Let’s Build Your Property Portfolio Together</div>
  <div class="abs accent-rule" style="left:0;width:212px;"></div>

  <div class="abs brand" style="left:36px;top:80px;"><span class="brand-square"></span><span>Oakridge<br>Capital Partners</span></div>

  <svg class="abs service-panel" viewBox="0 0 288 209" role="img" aria-label="Seven-step 360 degree service cycle over a dusk photo of a modern home with pool">
    <rect width="288" height="209" fill="var(--night)"/>
    <g font-family="Arimo, sans-serif" text-anchor="middle" fill="#fff">
      <g transform="translate(144,106)">
        <circle r="46" fill="none" stroke="#fff" stroke-width="1" opacity=".5"/>
        <g fill="var(--blue)" stroke="#fff" stroke-width="1.5">
          <circle cx="0" cy="-68" r="23"/><circle cx="53" cy="-42" r="23"/><circle cx="66" cy="15" r="23"/>
          <circle cx="30" cy="61" r="23"/><circle cx="-30" cy="61" r="23"/><circle cx="-66" cy="15" r="23"/><circle cx="-53" cy="-42" r="23"/>
        </g>
        <circle r="34" fill="var(--night)" stroke="#fff" stroke-width="3"/>
        <text y="-3" font-size="13" font-weight="700" fill="var(--blue)">360°</text>
        <text y="13" font-size="12" font-weight="700" fill="var(--blue)">Service</text>
        <g font-size="11"><text x="0" y="-71">1</text><text x="53" y="-45">2</text><text x="66" y="12">3</text><text x="30" y="58">4</text><text x="-30" y="58">5</text><text x="-66" y="12">6</text><text x="-53" y="-45">7</text></g>
        <g font-size="4.3">
          <text x="0" y="-61">Assess Finance</text><text x="0" y="-56">Capacity</text>
          <text x="53" y="-35">Establish Property</text><text x="53" y="-30">Goals</text>
          <text x="66" y="22">Evaluate Property</text><text x="66" y="27">Strategy</text>
          <text x="30" y="68">Identify Market</text>
          <text x="-30" y="68">Find Suitable</text><text x="-30" y="73">Property</text>
          <text x="-66" y="22">Purchase</text>
          <text x="-53" y="-35">Rent &amp; Manage</text>
        </g>
      </g>
    </g>
  </svg>
  <div class="abs panel-tab"></div>

  <h1 class="abs heading intro-title">We Are There</h1>
  <h2 class="abs heading intro-sub">Every Step Of The Way</h2>
  <p class="abs intro-copy">We don’t just find you a great investment property, we are there every step of the journey to ensure a seamless stress free experience.</p>

  <div class="abs padlock" role="img" aria-label="Photo of a silver combination padlock with a blue dial"></div>

  <div class="abs invested-band">
    <div class="heading big">We Are</div>
    <div class="heading small">Invested With You.</div>
  </div>

  <div class="abs kicker guarantee-label">Security</div>
  <h2 class="abs heading guarantee-title">4 Year Rent Guarantee</h2>

  <div class="abs guarantee-copy">
    <p>We provide a 4 year rent guarantee on selected properties. One week after the completion of your new property OCP will pay you an agreed market rent for 4 straight years. No need to worry about finding tenants or collecting rent, we have that covered.</p>
    <p>OCP will take on the task of sourcing tenants and collecting rent on your behalf. Any short falls in rent or vacancy periods will be at OCP expense. Meaning for the first 4 years we are taking on the rental risk, hence the phrase “We are invested with you”!</p>
    <p>Contact OCP for further details on the terms and conditions of this offer.</p>
  </div>

  <div class="abs heading risk-bar">We Help Minimise Your Risk</div>
  <div class="abs risk-rule"></div>

  <div class="abs benefit" style="left:25px;">
    <div class="benefit-icon"><svg width="20" height="20" viewBox="0 0 20 20" fill="none" stroke="#fff" stroke-width="1.4"><circle cx="10" cy="8" r="5"/><path d="M7 12l-2 6 3-1.5 2 2M13 12l2 6-3-1.5-2 2"/></svg></div>
    <div class="benefit-label">Low Risk Locations</div>
  </div>
  <div class="abs benefit" style="left:155px;">
    <div class="benefit-icon"><svg width="20" height="20" viewBox="0 0 20 20" fill="none" stroke="#fff" stroke-width="1.4"><rect x="3" y="3" width="14" height="14"/><path d="M7 14v-3M10 14V7M13 14V9"/></svg></div>
    <div class="benefit-label">Sourced Direct</div>
  </div>
  <div class="abs benefit" style="left:285px;">
    <div class="benefit-icon"><svg width="20" height="20" viewBox="0 0 20 20" fill="none" stroke="#fff" stroke-width="1.4"><circle cx="10" cy="10" r="7"/><path d="M13 7l-2 4-4 2 2-4z"/></svg></div>
    <div class="benefit-label">Real Investors</div>
  </div>
  <div class="abs benefit" style="left:405px;">
    <div class="benefit-icon"><svg width="20" height="20" viewBox="0 0 20 20" fill="none" stroke="#fff" stroke-width="1.4"><circle cx="13" cy="7" r="3.5"/><path d="M10.5 9.5L4 16l1.5 1.5M6 14l1.5 1.5"/></svg></div>
    <div class="benefit-label">Full Turn Key</div>
  </div>

  <!-- Right page -->
  <div class="abs tagline-bar right">Let’s Build Your Property Portfolio Together</div>
  <div class="abs accent-rule" style="left:598px;width:190px;"></div>

  <h1 class="abs heading page-title">Property Type</h1>
  <div class="abs brand right-brand"><span class="brand-square"></span><span>Oakridge<br>Capital Partners</span></div>

  <section class="abs property" style="top:133px;">
    <div class="tag">Secure Investment</div>
    <h3 class="name">House And Land</h3>
    <p>Full turn key house and land packages are the most popular choice of OCP investors. Houses generally provide stronger growth then apartments and appeal to a wider array of people. Also, whilst the gross rent return can at times be lower than apartments, this is generally offset by the fact there are no body corporate fees. This often results in leaving the net return of houses higher then apartments.</p>
    <p>With full turnkey packages starting from the $319,900 for 4 bedroom 2 bathroom houses, it is easy to see the value in this asset class.</p>
  </section>

  <section class="abs property" style="top:321px;">
    <div class="tag">Positive Cash Flow</div>
    <h3 class="name">Dual Dwelling</h3>
    <p>Dual dwellings are a relatively new concept and only available within certain councils around Australia. From the outside they look like a normal house, however, on the inside they are actually two separate rental houses, similar to a duplex. Although, unlike a duplex they cannot be sold off separately. On a positive, they are on the one title so no need for duplicate council fees, plus they are generally much cheaper than a duplex.</p>
    <p>The major attribute of this type of property is the huge rental income derived from two dwellings. This places the majority of these types of investments into the cash flow positive category. Due to this, these properties may be best suited to investors that have lots of equity but are low on cash flow.</p>
  </section>

  <section class="abs property" style="top:543px;">
    <div class="tag">Increasing Demand</div>
    <h3 class="name" style="margin-bottom:1px;">Apartments</h3>
    <p>Apartments are emerging as a very good option for property investors. Although in the past they have generally been outperformed by houses in regards to growth. Research shows changing demographics are leading to apartments becoming a more popular choice for a growing number of people. Evidence suggests that an aging population and the preference to downsize could also lead to a greater demand for apartments.</p>
    <p>Another major benefit which has emerged recently is the ability to purchase apartments through a Self-Managed Super Fund (SMSF), which is also becoming very popular among investors. Along with these benefits is also the fact that apartments will generally have lower maintenance and be in more premium locations then houses at the same price bracket. For these reasons apartments may be the ideal investment for some.</p>
  </section>

  <div class="abs tablet-view" style="top:178px;height:110px;background:linear-gradient(135deg,#d8dde2,#5d6b78 55%,#2d3640);" role="img" aria-label="Tablet showing a modern single-storey house and land package"></div>
  <div class="abs tablet-view" style="top:370px;height:128px;background:linear-gradient(135deg,#d8dde2,#6a7785 50%,#2f3944);" role="img" aria-label="Tablet showing a two-storey dual dwelling home at dusk"></div>
  <div class="abs tablet-view" style="left:1020px;top:563px;width:140px;height:176px;background:linear-gradient(180deg,#7fa8cf,#3b5f86 45%,#b77a4a);" role="img" aria-label="Tablet showing a modern apartment tower with a caption about apartments for investors"></div>

  <div class="abs site-footer"></div>
  <div class="abs footer-url" style="left:0;">www.oakridgecapitalpartners.example</div>
  <div class="abs footer-url" style="left:600px;">www.oakridgecapitalpartners.example</div>
</main>
</body>
</html>
```